the look of import selling star-up company

I have attached rhino logo that i like (can be edit) and i wanna turn that in to luxury look. Example like black base and gold logo +luxury looking font.

Company name: Brevan trading Oy
Slogan: Exceptional is the standard.
CEO Juho Kettumaa
Starting to import ceramic nano coatings to cars, in home use and industrial purposes.

Target Market(s)

30-60 year old men and women ho have big money and know what car they drive

Industry/Entity Type

It Company

```html
<!DOCTYPE html>
<html lang="en">
<head>
<meta charset="utf-8">
<title>Brevan trading Oy — Stationery</title>
<link rel="stylesheet" href="https://fonts.googleapis.com/css2?family=Roboto:wght@400;500;700&display=swap">
<style>
:root{
  --bg:#f1f1f1;
  --paper:#f7f7f7;
  --ink:#1a1a1a;
  --muted:#555;
  --black:#050505;
  --spine:#3b3b3b;
  --gold:#c9a43a;
  --white:#f4f4f4;
}
*{margin:0;padding:0;box-sizing:border-box}
html,body{width:1200px;height:795px;overflow:hidden}
body{background:var(--bg);font-family:"Roboto",Arial,sans-serif;color:var(--ink);position:relative}
.piece{position:absolute}
.brand{color:var(--gold);font-weight:500;font-family:"Roboto",Arial,sans-serif;text-align:center;line-height:1.15;display:flex;align-items:center;justify-content:center;gap:4px}
.brand .dot{width:5px;height:5px;border-radius:50%;background:var(--gold);flex:none}
.tab{position:absolute;top:0;background:var(--black);border-radius:0 0 22px 22px;display:flex;align-items:center;justify-content:center;padding:0 3px}

/* Letterhead */
.letterhead{left:292px;top:99px;width:293px;height:414px;background:var(--paper)}
.letterhead .tab{left:227px;width:44px;height:67px}
.letterhead .tab .brand{font-size:6px}
.letter-greeting{position:absolute;left:21px;top:106px;font-size:7.5px;color:var(--ink)}
.letter-body{position:absolute;left:21px;top:131px;width:251px;font-size:4.7px;line-height:6.9px;color:#333}
.letter-body p{margin-bottom:4.5px;text-align:justify}
.letter-close{position:absolute;left:21px;top:281px;font-size:4.2px;color:#333}
.letter-sign{position:absolute;left:21px;top:294px;width:40px;height:12px;background:linear-gradient(90deg,#d8d8d8,#eaeaea)}
.letter-rule{position:absolute;left:21px;right:21px;top:362px;height:1px;background:#555}
.letter-foot{position:absolute;top:372px;font-size:4.4px;line-height:6px;color:#444;font-style:normal}
.letter-foot.left{left:21px;top:376px}
.letter-foot.right{right:21px;text-align:right}
.icon{display:inline-block;width:4px;height:4px;background:#333;margin-left:2px;vertical-align:middle;border-radius:1px}

/* Folder */
.folder{left:636px;top:80px;width:347px;height:437px;background:var(--black)}
.folder .spine{position:absolute;left:0;top:0;width:19px;height:100%;background:var(--spine)}
.folder .brand{position:absolute;left:19px;right:0;top:205px;font-size:22px;gap:10px}
.folder .brand .dot{width:14px;height:14px}
.folder .tagline{position:absolute;left:19px;right:0;top:391px;text-align:center;color:var(--white);font-size:10.5px;letter-spacing:.3px}

/* Business cards */
.card-front{left:186px;top:550px;width:133px;height:75px;background:var(--paper)}
.card-front .tab{left:88px;width:39px;height:44px;border-radius:0 0 18px 18px}
.card-front .brand{font-size:5px}
.card-name{position:absolute;left:6px;top:38px;font-size:4.6px;font-weight:700}
.card-role{position:absolute;left:6px;top:44px;font-size:3px;color:var(--muted)}
.card-rule{position:absolute;left:6px;right:6px;top:50px;height:.6px;background:#777}
.card-contact{position:absolute;top:53px;font-size:2.8px;line-height:3.8px;color:#333;font-style:normal}
.card-contact.left{left:6px}
.card-contact.right{right:6px;text-align:right}
.card-back{left:186px;top:647px;width:133px;height:75px;background:var(--black)}
.card-back .brand{position:absolute;left:0;right:0;top:28px;font-size:7px}
.card-back .tagline{position:absolute;left:0;right:0;top:63px;text-align:center;color:var(--white);font-size:3px}

/* Envelopes */
.envelope-front{left:354px;top:561px;width:327px;height:157px;background:var(--paper)}
.envelope-front .tab{left:17px;width:41px;height:53px;border-radius:0 0 20px 20px}
.envelope-front .brand{font-size:5.5px}
.envelope-address{position:absolute;left:17px;top:60px;font-size:4.4px;line-height:5.6px;color:#444;font-style:normal}
.envelope-back{left:713px;top:561px;width:329px;height:157px;background:var(--paper)}
.envelope-back .flap{position:absolute;left:0;top:0;width:100%;height:55px;background:var(--black);border-radius:0 0 12px 12px}
.envelope-back .brand{position:absolute;left:0;right:0;top:20px;font-size:6px}
.envelope-back .tagline{position:absolute;left:0;right:0;top:39px;text-align:center;color:var(--white);font-size:3px}
</style>
</head>
<body>

<section class="piece letterhead">
  <div class="tab"><div class="brand">Brevan trading Oy</div></div>
  <p class="letter-greeting">Dear Mr. Lindqvist,</p>
  <div class="letter-body">
    <p>Thank you for your interest in our ceramic nano coatings. We import premium surface protection for cars, homes and industrial sites, selected for owners who expect a lasting deep gloss and real durability from every product they choose. Each formula is sourced from trusted laboratories and checked by our own team before it reaches a single customer in the region.</p>
    <p>Our range is tested in harsh northern conditions and applied by trained partners only. Every coating bonds with paint, glass and metal to resist dirt, salt, water and daily wear for years, keeping the finish bright while cutting the time spent on washing and care of the whole surface.</p>
    <p>We would be glad to arrange a private demonstration at a time and place that suits you best. Our specialist will walk you through each option, explain how the layers are built and cured, and help you choose the right finish for your vehicle, your home or your business premises. After the work is done we provide a written care guide, a full warranty certificate and a follow-up visit within the first three months to confirm the result meets our standard.</p>
    <p>Please contact us directly to book a meeting or to request our full catalogue and price list for the coming season. We look forward to hearing from you and to protecting what you value most.</p>
  </div>
  <p class="letter-close">Sincerely,</p>
  <div class="letter-sign" role="img" aria-label="Handwritten signature"></div>
  <div class="letter-rule"></div>
  <address class="letter-foot left">1420 Harbor Street<br>Portland, Oregon 97201<br>www.brevantrading.com</address>
  <div class="letter-foot right">
    555 210 4831<span class="icon"></span><br>
    555 317 6620<span class="icon"></span><br>
    555 408 2257<span class="icon"></span><br>
    juho@brevantrading.com<span class="icon"></span>
  </div>
</section>

<section class="piece folder">
  <div class="spine"></div>
  <div class="brand"><span class="dot"></span>Brevan trading Oy</div>
  <p class="tagline">EXCEPTIONAL IS THE STANDARD.</p>
</section>

<section class="piece card-front">
  <div class="tab"><div class="brand">Brevan trading Oy</div></div>
  <p class="card-name">JUHO KETTUMAA</p>
  <p class="card-role">CEO</p>
  <div class="card-rule"></div>
  <div class="card-contact left">555 210 4831<br>555 317 6620<br>555 408 2257<br>juho@brevantrading.com</div>
  <address class="card-contact right">1420 Harbor Street<br>Portland, Oregon 97201<br>www.brevantrading.com</address>
</section>

<section class="piece card-back">
  <div class="brand"><span class="dot"></span>Brevan trading Oy</div>
  <p class="tagline">EXCEPTIONAL IS THE STANDARD</p>
</section>

<section class="piece envelope-front">
  <div class="tab"><div class="brand">Brevan trading Oy</div></div>
  <address class="envelope-address">1420 Harbor Street<br>Portland, Oregon 97201</address>
</section>

<section class="piece envelope-back">
  <div class="flap"></div>
  <div class="brand"><span class="dot"></span>Brevan trading Oy</div>
  <p class="tagline">EXCEPTIONAL IS THE STANDARD</p>
</section>

</body>
</html>
```